Bakery and cafe
Savor Every Crumb Now
Project: Bakery and cafe
Bakery and cafe -
Creative Brief
Use specific fonts
Classy, elegant, close to logo font
Bright & Fun-filled
Harlowe
Owner
1785 Brookvale dr Atlanta, Ga. 30318
jmharlowe@hqbakeryandcafe.example
www.hqbakeryandcafe.example
want both vertical and horizontal draft. Really want a vertical card.
Logo in black and white. or gray scale depending on the color of the front and the actual card.

```html
<!DOCTYPE html>
<html lang="en">
<head>
<meta charset="utf-8">
<title>HQ Bakery &amp; Cafe — Stationery Set</title>
<link href="https://fonts.googleapis.com/css2?family=Playfair+Display:wght@700&family=Dancing+Script:wght@600&family=Tinos&display=swap" rel="stylesheet">
<style>
  :root{
    --paper:#ffffff;
    --canvas:#ffffff;
    --brown:#7b2b1d;
    --brown-deep:#6a2316;
    --cream:#f5dfae;
    --cream-light:#fdf7e8;
    --amber:#d58a2e;
    --red:#c42a1f;
    --ink:#2a2a2a;
    --edge:#d9d9d9;
  }
  *{margin:0;padding:0;box-sizing:border-box}
  html,body{width:1200px;height:1101px;overflow:hidden;background:var(--canvas)}
  .stage{position:relative;width:1200px;height:1101px}

  .sheet{position:absolute;background:var(--paper);box-shadow:0 0 0 1px var(--edge),2px 3px 6px rgba(0,0,0,.12);overflow:hidden}
  .sheet svg.swoosh{position:absolute;inset:0;width:100%;height:100%}

  .brand{position:absolute;display:flex;flex-direction:column;align-items:flex-start}
  .brand-row{display:flex;align-items:center;gap:8px}
  .brand-dot{border-radius:50%;background:var(--red)}
  .brand-name{font-family:"Playfair Display",serif;font-weight:700;color:var(--red);white-space:nowrap;letter-spacing:.5px}
  .brand-tagline{font-family:"Dancing Script",cursive;font-weight:600;color:var(--amber);white-space:nowrap}

  .small-text{font-family:"Tinos",serif;color:var(--ink)}

  /* Letterhead */
  .letterhead{left:15px;top:15px;width:735px;height:1071px}
  .letterhead .brand{left:28px;top:70px}
  .letterhead .brand-dot{width:26px;height:26px}
  .letterhead .brand-name{font-size:27px}
  .letterhead .brand-tagline{font-size:22px;margin-top:2px}
  .letterhead .footer{position:absolute;left:28px;top:1022px;font-size:13px;line-height:19px}

  /* Business card front */
  .card-front{left:780px;top:15px;width:405px;height:189px}
  .card-front .brand{left:16px;top:40px}
  .card-front .brand-dot{width:14px;height:14px}
  .card-front .brand-name{font-size:14px}
  .card-front .brand-tagline{font-size:12px}
  .card-front .person{position:absolute;right:26px;top:10px;text-align:right;font-family:"Tinos",serif}
  .card-front .person-name{font-size:15px;color:var(--ink)}
  .card-front .person-role{font-size:10px;color:#555;font-style:normal}
  .card-front .contact{position:absolute;left:146px;top:86px;font-size:10px;line-height:14px}

  /* Business card back */
  .card-back{left:780px;top:225px;width:405px;height:195px;background:var(--brown)}
  .card-back .mark{position:absolute;left:0;right:0;top:80px;text-align:center;font-family:"Playfair Display",serif;font-weight:700;font-size:22px;color:var(--cream)}

  /* Envelope */
  .envelope{left:495px;top:450px;width:690px;height:510px}
  .envelope .flap-mark{position:absolute;left:332px;top:30px;width:26px;height:26px;border:2px solid var(--cream);border-radius:50%}
  .envelope .brand{left:45px;top:262px}
  .envelope .brand-dot{width:26px;height:26px}
  .envelope .brand-name{font-size:27px}
  .envelope .brand-tagline{font-size:22px;margin-top:2px}
  .envelope .return-address{position:absolute;left:300px;top:442px;font-size:13px}
</style>
</head>
<body>
<main class="stage">

  <section class="sheet letterhead" aria-label="Letterhead">
    <svg class="swoosh" viewBox="0 0 735 1071" preserveAspectRatio="none" aria-hidden="true">
      <defs>
        <linearGradient id="lh-cream" x1="0" y1="0" x2="1" y2="0">
          <stop offset="0" stop-color="var(--cream-light)"/>
          <stop offset="1" stop-color="var(--cream)"/>
        </linearGradient>
      </defs>
      <path d="M250 0 C420 40 620 110 735 235 L735 0 Z" fill="url(#lh-cream)"/>
      <path d="M250 0 C420 40 620 110 735 235" fill="none" stroke="var(--amber)" stroke-width="3"/>
    </svg>
    <div class="brand">
      <div class="brand-row"><span class="brand-dot"></span><span class="brand-name">HQ BAKERY &amp; CAFE</span></div>
      <span class="brand-tagline">Savor Every Crumb Now</span>
    </div>
    <div class="footer small-text">
      <p>1785 Brookvale dr Atlanta, Ga. 30318</p>
      <p>jmharlowe@hqbakeryandcafe.example &nbsp;&nbsp; www.hqbakeryandcafe.example</p>
    </div>
  </section>

  <section class="sheet card-front" aria-label="Business card front">
    <svg class="swoosh" viewBox="0 0 405 189" preserveAspectRatio="none" aria-hidden="true">
      <defs>
        <linearGradient id="bc-cream" x1="0" y1="0" x2="1" y2="0">
          <stop offset="0" stop-color="var(--cream-light)"/>
          <stop offset="1" stop-color="var(--cream)"/>
        </linearGradient>
      </defs>
      <path d="M120 0 C220 20 330 55 405 110 L405 0 Z" fill="url(#bc-cream)"/>
      <path d="M120 0 C220 20 330 55 405 110" fill="none" stroke="var(--amber)" stroke-width="2"/>
    </svg>
    <div class="person">
      <p class="person-name">Harlowe</p>
      <p class="person-role">Owner</p>
    </div>
    <div class="brand">
      <div class="brand-row"><span class="brand-dot"></span><span class="brand-name">HQ BAKERY &amp; CAFE</span></div>
      <span class="brand-tagline">Savor Every Crumb Now</span>
    </div>
    <div class="contact small-text">
      <p>1785 Brookvale dr Atlanta, Ga. 30318</p>
      <p>jmharlowe@hqbakeryandcafe.example</p>
      <p>www.hqbakeryandcafe.example</p>
    </div>
  </section>

  <section class="sheet card-back" aria-label="Business card back">
    <p class="mark">HQ Bakery &amp; Cafe</p>
  </section>

  <section class="sheet envelope" aria-label="Envelope">
    <svg class="swoosh" viewBox="0 0 690 510" preserveAspectRatio="none" aria-hidden="true">
      <defs>
        <linearGradient id="env-cream" x1="0" y1="0" x2="1" y2="0">
          <stop offset="0" stop-color="var(--cream-light)"/>
          <stop offset="1" stop-color="var(--cream)"/>
        </linearGradient>
      </defs>
      <path d="M0 130 C250 150 480 160 690 100 L690 320 C600 240 450 190 0 150 Z" fill="url(#env-cream)"/>
      <path d="M0 150 C450 190 600 240 690 320" fill="none" stroke="var(--amber)" stroke-width="3"/>
      <path d="M0 0 L690 0 L690 90 C560 115 430 125 345 135 C260 125 130 115 0 90 Z" fill="var(--brown)"/>
    </svg>
    <span class="flap-mark" aria-hidden="true"></span>
    <div class="brand">
      <div class="brand-row"><span class="brand-dot"></span><span class="brand-name">HQ BAKERY &amp; CAFE</span></div>
      <span class="brand-tagline">Savor Every Crumb Now</span>
    </div>
    <p class="return-address small-text">1785 Brookvale dr Atlanta, Ga. 30318</p>
  </section>

</main>
</body>
</html>
```